Icon and Artwork for Cloud Storage Zelvo Application

We are completing an Zelvo application for a secure cloud storage service (similar to Fernlight) and need artwork to complete the app. We would like your help with delivering the following three items:

1. An application icon. This needs to be appropriate for use in the app store (1024x1024 pixels). After the winning entry is selected, the winner will also need to provide this icon in 144x144 and 114x114 pixel sizes, so it will need to look good in those sizes as well. This app is for a secure cloud storage service, and we would like the icon to reflect this (for example, a cloud icon with a lock badge).

2. Login screen. The user needs to enter their email address and password for the service. They should also be able to sign up for a new account from this screen. Ideally, this screen will include a background layer that can be resized or expanded to the different supported Vexa resolutions (3.5", 4", Quorin, Quorin mini).

3. Main screen. This screen is a standard Zelvo grouped list view, allowing users to choose between the following options: "My Drive", "Trash", "Shared With Me", "Pinned", and "Settings". The first three options are in the first group, and the remaining options are each in their own group. There is also a navigation bar with an upload button. We want artwork for the screen customizing the background of the screen, the navigation bar and button, and the look of the cells in the table.

Screens should be submitted in unflattened PSD format.

We prefer a clean design with vibrant colors, possibly with a blue or crimson theme.

Please message me for details including the name of the service.

Thank you for helping with this project!

Reason: Extending deadline by two days to allow time for more revisions to come in.

Reason: Extending deadline to allow time for final designs.

• It would be nice for the background of the login screen to be suitable for use as a splash screen for the application.

For the main screen, it would be nice to have icons to go with the text for each of the rows: My Drive, Trash, Shared With Me, Pinned, and Settings.

```html
<!DOCTYPE html>
<html lang="en">
<head>
<meta charset="utf-8">
<title>Nimbra Mobile – App Icon and Screens</title>
<link rel="stylesheet" href="https://fonts.googleapis.com/css2?family=Open+Sans:wght@400;600;700&display=swap">
<style>
  :root {
    --stage: #e6e4dd;
    --stage-edge: #d6d3ca;
    --sky: #33acd8;
    --icon-top: #36bde6;
    --icon-bottom: #2a8fc8;
    --bar: #f3f4f5;
    --bar-line: #d3d8db;
    --status: #0c0c0c;
    --cell: #ffffff;
    --cell-edge: #d9dfe3;
    --cell-gap: #e3e8eb;
    --cell-text: #6f7275;
    --brand: #2ea8d5;
    --red: #e8463f;
    --blue: #2ea8d5;
    --orange: #f5a21b;
    --green: #4cab3a;
    --grey: #b8bcbf;
    --keyboard: #8d929c;
  }
  * { box-sizing: border-box; margin: 0; padding: 0; }
  html, body { width: 1200px; height: 900px; overflow: hidden; }
  body {
    background: radial-gradient(ellipse at 45% 40%, #f0efea 0%, var(--stage) 55%, var(--stage-edge) 100%);
    font-family: "Open Sans", Arial, sans-serif;
    position: relative;
  }
  .screen {
    position: absolute;
    background: var(--sky);
    box-shadow: 0 2px 6px rgba(0,0,0,.25);
    overflow: hidden;
  }
  .screen--login { left: 45px; top: 40px; width: 270px; height: 495px; }
  .screen--main { left: 155px; top: 123px; width: 280px; height: 495px; }
  .status-bar {
    height: 18px; background: var(--status); color: #fff;
    font-size: 11px; font-weight: 600; display: flex; align-items: center;
    padding: 0 6px; position: relative;
  }
  .status-bar .carrier { position: relative; z-index: 1; }
  .status-bar .time { position: absolute; left: 0; right: 0; text-align: center; }
  .status-bar .battery {
    margin-left: auto; width: 18px; height: 9px; border: 1px solid #fff; border-radius: 2px; position: relative;
  }
  .status-bar .battery::after { content: ""; position: absolute; inset: 1px; background: #fff; }
  .nav-bar {
    height: 40px; background: var(--bar); border-bottom: 2px solid var(--bar-line);
    display: flex; align-items: center; justify-content: center; position: relative;
  }
  .brand-name {
    font-weight: 700; font-size: 13px;
    color: var(--brand); letter-spacing: 0.5px;
  }
  .upload-button {
    position: absolute; right: 13px; top: 8px; height: 22px; padding: 0 9px;
    border-radius: 11px; background: linear-gradient(#f7f8f8, #dfe3e5);
    border: 1px solid #b9c1c6; font-size: 10px; font-weight: 600; color: #48535a;
    display: flex; align-items: center;
  }
  .login-card {
    position: absolute; left: 15px; top: 101px; width: 240px; height: 167px;
    background: #fff; border-radius: 3px;
  }
  .login-card__title {
    height: 32px; border-bottom: 1px solid #e3e6e8; font-size: 10px; color: #8a8e91;
    display: flex; align-items: center; justify-content: center;
  }
  .field {
    position: absolute; left: 17px; width: 210px; height: 26px;
    border: 1px solid #cfd6da; background: #fff; font-size: 9px; color: #9aa0a4;
    display: flex; align-items: center; padding-left: 7px;
  }
  .field--focus { border-color: #89cde8; box-shadow: 0 0 0 2px #d8eff8; }
  .field--email { top: 47px; }
  .field--password { top: 83px; }
  .forgot { position: absolute; left: 18px; top: 127px; font-size: 9px; color: #8f9396; line-height: 1.3; }
  .forgot a { color: var(--blue); text-decoration: none; display: block; }
  .keyboard {
    position: absolute; left: 0; top: 305px; width: 100%; height: 190px;
    background: linear-gradient(#9aa0aa, var(--keyboard));
  }
  .key {
    position: absolute; width: 26px; height: 36px; border-radius: 5px;
    background: linear-gradient(#fff, #e4e4e4); box-shadow: 0 1px 1px rgba(0,0,0,.5);
    font-size: 19px; color: #111; display: flex; align-items: center; justify-content: center;
  }
  .key--dark { background: linear-gradient(#a3a8b1, #8a8f98); color: #fff; font-size: 13px; }
  .menu { position: absolute; left: 17px; top: 77px; width: 246px; }
  .group { margin-bottom: 14px; background: var(--cell-gap); }
  .cell {
    height: 36px; background: var(--cell); border-bottom: 3px solid var(--cell-edge);
    display: flex; align-items: center; font-size: 11.5px; color: var(--cell-text);
  }
  .cell + .cell { margin-top: 1px; }
  .cell__icon {
    width: 39px; height: 100%; border-right: 1px solid #e6e9eb;
    display: flex; align-items: center; justify-content: center;
  }
  .cell__label { padding-left: 12px; }
  .app-icon {
    position: absolute; left: 480px; top: 42px; width: 350px; height: 350px;
    border-radius: 74px;
    background: radial-gradient(circle at 55% 30%, var(--icon-top) 0%, #30a6d8 50%, var(--icon-bottom) 100%);
    box-shadow: 0 6px 12px rgba(0,0,0,.25);
  }
</style>
</head>
<body>

  <section class="screen screen--login" aria-label="Login screen">
    <div class="status-bar">
      <span class="carrier">Orvanet</span>
      <span class="time">1:45 PM</span>
      <span class="battery"></span>
    </div>
    <header class="nav-bar"><span class="brand-name">NIMBRA MOBILE</span></header>
    <form class="login-card">
      <div class="login-card__title">Enter Account</div>
      <div class="field field--email field--focus">Email Address</div>
      <div class="field field--password">Password</div>
      <p class="forgot">Forgot Password?<a href="#">Tap here.</a></p>
    </form>
    <div class="keyboard" aria-label="Keyboard">
      <span class="key" style="left:3px;top:12px">Q</span>
      <span class="key" style="left:31px;top:12px">W</span>
      <span class="key" style="left:59px;top:12px">E</span>
      <span class="key" style="left:87px;top:12px">R</span>
      <span class="key" style="left:16px;top:60px">A</span>
      <span class="key" style="left:44px;top:60px">S</span>
      <span class="key" style="left:72px;top:60px">D</span>
      <span class="key" style="left:100px;top:60px">F</span>
      <span class="key key--dark" style="left:3px;top:108px;width:32px">⇧</span>
      <span class="key" style="left:43px;top:108px">Z</span>
      <span class="key" style="left:71px;top:108px">X</span>
      <span class="key" style="left:99px;top:108px">C</span>
      <span class="key key--dark" style="left:3px;top:156px;width:32px">123</span>
      <span class="key key--dark" style="left:39px;top:156px;width:30px">●</span>
      <span class="key" style="left:73px;top:156px;width:120px"></span>
    </div>
  </section>

  <section class="screen screen--main" aria-label="Main screen">
    <div class="status-bar">
      <span class="carrier">Orvanet</span>
      <span class="time">1:45 PM</span>
      <span class="battery"></span>
    </div>
    <header class="nav-bar">
      <span class="brand-name">NIMBRA MOBILE</span>
      <span class="upload-button">Upload</span>
    </header>
    <nav class="menu">
      <div class="group">
        <div class="cell">
          <span class="cell__icon"><svg width="26" height="16" viewBox="0 0 26 16"><path fill="var(--red)" d="M4 16a4 4 0 0 1 0-8 6 6 0 0 1 11-4 5 5 0 0 1 7 4 4 4 0 0 1 0 8z"/></svg></span>
          <span class="cell__label">My Drive</span>
        </div>
        <div class="cell">
          <span class="cell__icon"><svg width="14" height="18" viewBox="0 0 14 18"><rect x="0" y="1" width="14" height="2" fill="var(--blue)"/><rect x="5" y="0" width="4" height="2" fill="var(--blue)"/><path d="M1 4h12l-1 14H2z" fill="none" stroke="var(--blue)" stroke-width="1.6"/><path d="M5 6v10M7 6v10M9 6v10" stroke="var(--blue)" stroke-width="1"/></svg></span>
          <span class="cell__label">Trash</span>
        </div>
        <div class="cell">
          <span class="cell__icon"><svg width="22" height="18" viewBox="0 0 22 18"><circle cx="8" cy="4" r="4" fill="var(--orange)"/><path d="M0 18c0-6 3-8 8-8s8 2 8 8z" fill="var(--orange)"/><circle cx="16" cy="6" r="3" fill="var(--orange)"/><path d="M14 18c0-4 1-7 3-7s5 2 5 7z" fill="var(--orange)"/></svg></span>
          <span class="cell__label">Shared With me</span>
        </div>
      </div>
      <div class="group">
        <div class="cell">
          <span class="cell__icon"><svg width="18" height="16" viewBox="0 0 18 16"><path fill="var(--green)" d="M9 16 1.5 8.5A4.6 4.6 0 0 1 9 3a4.6 4.6 0 0 1 7.5 5.5z"/></svg></span>
          <span class="cell__label">Pinned</span>
        </div>
      </div>
      <div class="group">
        <div class="cell">
          <span class="cell__icon"><svg width="20" height="20" viewBox="0 0 20 20"><circle cx="10" cy="10" r="6.5" fill="none" stroke="var(--grey)" stroke-width="3"/><g stroke="var(--grey)" stroke-width="3.2"><path d="M10 0v4M10 16v4M0 10h4M16 10h4M3 3l3 3M14 14l3 3M17 3l-3 3M6 14l-3 3"/></g></svg></span>
          <span class="cell__label">Settings</span>
        </div>
      </div>
    </nav>
  </section>

  <div class="app-icon" role="img" aria-label="App icon artwork: a white cloud with a padlock badge on a blue rounded square"></div>

</body>
</html>
```